Business Card for Wholesale Comapany
Pelvo Goods
Business Card for Wholesale Comapany - Construction
Creative Brief
Professional
Mark Tilney
Chief Sales Officer
8142-C Marlow Ridge Boulevard #310 Houston, TX. 77031-2287
mtilney@pelvogoods.example
www.pelvogoods.example
Your design can be for one or both sides of the card, I do not have a preference. I just completed the contest for my logo design and as soon as the .ai file is sent to me I will forward. But, for the time being, you can find my logo at http://www.brakenstudio.example/drafts/display/contest/519274/draft/7a1c04be92d3f65e08b1c7a94f3e2d60b815937.
rkanto41q rkanto41q
Here is the .ai file for the logo, so hopefully this will make it easier for you designs. Also, some great designs have been submitted and here are some items I have gravitated to: 1. I am going to want rounded corners. 2. I like the idea of having a 2 sided card. 3. On the back, almost all designs have come in black. I would like to see another color used, or make a statement with design on a white background. 4. Don't be too heavily skewed to the professional type of card. Thanks
VelMar VelMar
What font did you use sir?

```html
<!DOCTYPE html>
<html lang="en">
<head>
<meta charset="utf-8">
<title>Pelvo Goods – Business Card</title>
<link rel="stylesheet" href="https://fonts.googleapis.com/css2?family=Open+Sans:wght@400;600;700&display=swap">
<style>
  :root {
    --stage: #ecebe8;
    --paper: #ffffff;
    --sand: #cbb48f;
    --bronze: #a57d3e;
    --ink: #3b2f22;
    --cocoa: #4a3320;
    --brand-gold: #9b7640;
  }
  * { margin: 0; padding: 0; box-sizing: border-box; }
  html, body {
    width: 1200px; height: 909px; overflow: hidden;
    background: var(--stage);
    font-family: "Open Sans", Arial, sans-serif;
  }
  .canvas { position: relative; width: 1200px; height: 909px; }
  .card {
    position: absolute; top: 155px;
    width: 340px; height: 600px;
    border-radius: 18px; overflow: hidden;
    box-shadow: 0 8px 24px rgba(0,0,0,0.15);
  }
  .card--front { left: 230px; background: var(--paper); }
  .card--back  { left: 630px; background: var(--sand); }
  .card-shape { position: absolute; inset: 0; width: 100%; height: 100%; }

  .brand {
    position: absolute; left: 0; right: 0;
    display: flex; align-items: center; justify-content: center; gap: 12px;
    font-weight: 700; font-size: 30px; letter-spacing: 0.5px; white-space: nowrap;
  }
  .brand-square { width: 30px; height: 30px; }
  .card--front .brand { top: 95px; color: var(--brand-gold); }
  .card--front .brand-square { background: var(--brand-gold); }
  .card--back .brand { top: 80px; color: var(--paper); }
  .card--back .brand-square { background: var(--sand); }

  .contact {
    position: absolute; top: 285px; left: 0; right: 0;
    text-align: center; color: var(--ink); font-size: 14px; line-height: 1.5;
  }
  .contact-name { font-weight: 700; font-size: 18px; }
  .contact-role { font-size: 15px; margin-bottom: 14px; }
  .contact-address { margin-bottom: 14px; }
  .contact-line b { font-weight: 700; }

  .back-web {
    position: absolute; bottom: 38px; left: 0; right: 0;
    text-align: center; color: var(--ink); font-size: 12px;
  }
</style>
</head>
<body>
<main class="canvas">

  <section class="card card--front">
    <svg class="card-shape" viewBox="0 0 340 600" preserveAspectRatio="none" aria-hidden="true">
      <path d="M0 262 Q170 190 340 232 L340 600 L0 600 Z" fill="var(--bronze)"/>
      <path d="M0 270 Q170 198 340 240 L340 600 L0 600 Z" fill="var(--sand)"/>
    </svg>
    <div class="brand"><span class="brand-square"></span>Pelvo Goods</div>
    <div class="contact">
      <p class="contact-name">Mark Tilney</p>
      <p class="contact-role">Chief Sales Officer</p>
      <p class="contact-address">8142-C Marlow Ridge Boulevard #310<br>Houston, TX. 77031-2287</p>
      <p class="contact-line"><b>Ph:</b> 012 555 0147</p>
      <p class="contact-line"><b>Cell:</b> 012 555 0147</p>
      <p class="contact-line"><b>Fax:</b> 012 555 0147</p>
      <p class="contact-line"><b>Email:</b> mtilney@pelvogoods.example</p>
      <p class="contact-line">www.pelvogoods.example</p>
    </div>
  </section>

  <section class="card card--back">
    <svg class="card-shape" viewBox="0 0 340 600" preserveAspectRatio="none" aria-hidden="true">
      <path d="M0 0 L340 0 L340 190 Q200 250 0 232 Z" fill="var(--bronze)"/>
      <path d="M0 0 L340 0 L340 180 Q200 240 0 222 Z" fill="var(--cocoa)"/>
    </svg>
    <div class="brand"><span class="brand-square"></span>Pelvo Goods</div>
    <p class="back-web">www.pelvogoods.example</p>
  </section>

</main>
</body>
</html>
```